Trade Show Booth Design for Saas company

Brightwave Post is a startup company that will be launching its software as a service product at a trade show in the near future. We are looking for something that really pops and is appealing to the eye. Attached is the branding guidelines along with the color palette. The pink should be predominant. We’re not so concerned with the copy of your design for the contest, but rather the design itself. We can work on the copy later. You can utilize any copy or graphics from our website at www.brightwavepost-example.com. You can also learn more about us at the website. One element from the website that is worth mentioning, and optional, is the hub and spoke graphic in the “Connect All Your SMTP Email Service Providers” section. (It is attached.) We will provide high resolution versions of anything you need. The display will be a flat 10 foot wide by 8 foot tall, one piece of fabric. We will also need the graphics for the 39in x 19in x 12in Counter Graphic Print, but probably just the logo on it. We are open to design elements that include the use of a person or not. We basically want something modern and very eye-catching.
Potential headline and text:
One place to manage it all
Guided by expert mailers, Brightwave Post combines every aspect of email marketing into a powerful package.

```html
<!DOCTYPE html>
<html lang="en">
<head>
<meta charset="utf-8">
<title>Brightwave Post – Trade Show Booth Graphics</title>
<link rel="stylesheet" href="https://fonts.googleapis.com/css2?family=Montserrat:wght@400;500;600;700;800&family=Noto+Sans:wght@400&display=swap">
<style>
  :root {
    --pink: #fc3a8c;
    --navy: #141a44;
    --cyan: #4ccdf2;
    --royal: #2f63b8;
    --paper: #f7f8fa;
    --mist: #eef1f6;
    --backdrop: #d9d9d9;
    --ink: #1d1d1d;
    --white: #ffffff;
  }
  * { box-sizing: border-box; margin: 0; padding: 0; }
  html, body { width: 1200px; height: 2421px; overflow: hidden; }
  body {
    background: var(--backdrop);
    font-family: "Montserrat", sans-serif;
    position: relative;
  }
  .panel {
    position: absolute;
    left: 133px;
    width: 933px;
    background: var(--paper);
    overflow: hidden;
    box-shadow: -6px 6px 8px rgba(0,0,0,0.35);
  }
  .backwall { top: 485px; height: 932px; }
  .counter { top: 1523px; height: 347px; }
  .decor { position: absolute; inset: 0; width: 100%; height: 100%; }
  .brand {
    position: absolute;
    left: 0; right: 0;
    display: flex;
    align-items: center;
    justify-content: center;
    gap: 18px;
    color: var(--navy);
    font-weight: 700;
    letter-spacing: 1px;
    white-space: nowrap;
  }
  .brand-mark { background: var(--pink); flex: none; }
  .backwall .brand { top: 160px; font-size: 58px; }
  .backwall .brand-mark { width: 54px; height: 54px; }
  .counter .brand { top: 105px; font-size: 46px; }
  .counter .brand-mark { width: 42px; height: 42px; }
  .headline {
    position: absolute;
    left: 0; right: 0; top: 333px;
    text-align: center;
    font-weight: 800;
    line-height: 62px;
    white-space: nowrap;
  }
  .headline .lead { display: block; color: var(--pink); font-size: 58px; }
  .headline .main { display: block; color: var(--navy); font-size: 62px; }
  .intro {
    position: absolute;
    left: 0; right: 0; top: 488px;
    text-align: center;
    font-size: 26px;
    line-height: 32px;
    color: var(--ink);
  }
  .feature {
    position: absolute;
    height: 52px;
    border: 2px solid var(--pink);
    background: var(--white);
    color: var(--navy);
    font-weight: 700;
    font-size: 22px;
    white-space: nowrap;
    display: flex; align-items: center; justify-content: center;
  }
  .feature.is-highlight { background: var(--pink); color: var(--white); border-color: var(--navy); }
  .contact-tag {
    position: absolute;
    left: 313px; top: 750px;
    width: 307px; height: 38px;
    border-radius: 19px;
    background: var(--navy);
    color: var(--white);
    font-size: 20px; font-weight: 500;
    white-space: nowrap;
    display: flex; align-items: center; justify-content: center;
  }
  .phone {
    position: absolute; left: 0; right: 0; top: 802px;
    text-align: center; color: var(--white);
    font-size: 44px; font-weight: 700; line-height: 50px;
    white-space: nowrap;
  }
  .contact-row {
    position: absolute; left: 0; right: 0; top: 868px;
    display: flex; justify-content: center; align-items: center; gap: 22px;
    color: var(--white); font-size: 20px; font-weight: 500;
    white-space: nowrap;
  }
  .contact-row .item { display: flex; align-items: center; gap: 8px; }
  .contact-row .divider { width: 2px; height: 32px; background: var(--white); }
  .counter-url {
    position: absolute; left: 0; right: 0; top: 292px;
    text-align: center; color: var(--white);
    font-size: 21px; letter-spacing: 1px;
    white-space: nowrap;
  }
  .size-label {
    position: absolute; left: 0; right: 0;
    text-align: center;
    font-family: "Noto Sans", sans-serif;
    font-size: 44px; color: var(--ink);
  }
  .size-wall { top: 1437px; }
  .size-counter { top: 1880px; }
</style>
</head>
<body>

<section class="panel backwall">
  <svg class="decor" viewBox="0 0 933 932" aria-hidden="true">
    <rect x="-120" y="60" width="260" height="140" rx="70" fill="#e9eef5" transform="rotate(-35 10 130)"/>
    <circle cx="40" cy="90" r="70" fill="var(--white)"/>
    <rect x="-140" y="250" width="230" height="90" rx="45" fill="var(--royal)" transform="rotate(-30 -25 295)"/>
    <rect x="740" y="50" width="330" height="150" rx="75" fill="var(--cyan)" transform="rotate(35 905 125)"/>
    <rect x="830" y="170" width="260" height="150" rx="75" fill="var(--white)" transform="rotate(35 960 245)"/>
    <path d="M0 852 Q466 692 933 852 L933 932 L0 932 Z" fill="var(--navy)"/>
    <path d="M0 862 Q466 702 933 862 L933 932 L0 932 Z" fill="var(--pink)"/>
  </svg>

  <div class="brand"><span class="brand-mark"></span>BRIGHTWAVE POST</div>

  <h1 class="headline">
    <span class="lead">ONE PLACE TO MANAGE</span>
    <span class="main">ALL YOUR EMAIL</span>
  </h1>

  <p class="intro">Guided by expert mailers, Brightwave Post combines every<br>aspect of email marketing into a powerful package.</p>

  <div class="feature" style="left:47px;top:570px;width:222px;">In-house SMTP</div>
  <div class="feature is-highlight" style="left:281px;top:570px;width:367px;">Multiple SMTP Connections</div>
  <div class="feature" style="left:658px;top:570px;width:227px;">Email Validation</div>
  <div class="feature" style="left:47px;top:634px;width:222px;">API Connections</div>
  <div class="feature" style="left:281px;top:634px;width:330px;">Reporting and Analytics</div>
  <div class="feature" style="left:621px;top:634px;width:264px;">Email Automation</div>

  <div class="contact-tag">CONTACT INFORMATION</div>
  <div class="phone">+1 (555) 014-2290</div>
  <div class="contact-row">
    <span class="item">
      <svg width="20" height="20" viewBox="0 0 24 24" aria-hidden="true" fill="none" stroke="#fff" stroke-width="2"><circle cx="12" cy="12" r="10"/><path d="M2 12h20M12 2c3 3 3 17 0 20M12 2c-3 3-3 17 0 20"/></svg>
      www.brightwavepost-example.com
    </span>
    <span class="divider"></span>
    <span class="item">
      <svg width="24" height="18" viewBox="0 0 26 20" aria-hidden="true"><rect width="26" height="20" rx="2" fill="#fff"/><path d="M1 2l12 9 12-9" fill="none" stroke="var(--pink)" stroke-width="2"/></svg>
      info@brightwavepost-example.com
    </span>
  </div>
</section>
<div class="size-label size-wall">10 foot by 10 foot</div>

<section class="panel counter">
  <svg class="decor" viewBox="0 0 933 347" aria-hidden="true">
    <rect x="-60" y="30" width="330" height="80" rx="40" fill="var(--cyan)" transform="rotate(-30 105 70)"/>
    <rect x="40" y="80" width="260" height="90" rx="45" fill="#eef2f8" transform="rotate(-30 170 125)"/>
    <rect x="-80" y="190" width="310" height="70" rx="35" fill="var(--royal)" transform="rotate(-30 75 225)"/>
    <rect x="690" y="40" width="330" height="130" rx="65" fill="var(--cyan)" transform="rotate(30 855 105)"/>
    <rect x="750" y="180" width="300" height="90" rx="45" fill="var(--white)" transform="rotate(30 900 225)"/>
    <path d="M0 343 Q466 185 933 343 L933 347 L0 347 Z" fill="var(--navy)"/>
    <path d="M0 347 Q466 195 933 347 Z" fill="var(--pink)"/>
  </svg>
  <div class="brand"><span class="brand-mark"></span>BRIGHTWAVE POST</div>
  <div class="counter-url">www.brightwavepost-example.com</div>
</section>
<div class="size-label size-counter">39in x 19in x 12in</div>

</body>
</html>
```